Kiswa Design

We need a flyer design for a product that we are a selling, a sacred Islamic cloth called a Kiswah, which is draped around the holy Kaaba in mecca every year.

The details we would like on the flyer are as follows:

Rare Kiswah of the holy Kaaba for sale (fitted in 1977 and 1982 vintage). For sale:

1) whole piece 15 meters x 2.60 meters : £60,000
2) 8 meters x 2.60 meters : £31,200
3) 4 meters x 2.60 meters : £15,600
4) 1 meter : £1500

(insert a high quality picture of holy Kaaba here, then underneath the picture, write the following:) "The Kaaba is covered by an expensive black cloth which is known as 'Kiswah' which is produced and changed every year"

(insert picture of our product here,i.e. use the document named MAIN IMAGE then underneath this picture write the following:) "Silk lampas weave Kiswah, woven silk on a black satin ground with Quranic calligraphy, the zig-zag bands of inscription alternate with the Shahadah and the inscription, 'God, exalted be His Glory!"

insert another picture of kiswah which i provided anywhere you like

(somewhere on flyer write the following) please note a percentage of sales will go towards Sadaqah for our Muslim brothers and sisters in need around the world

(somewhere on flyer write the following) Harwell's international auction house authenticity document also available to prove the Kiswah is genuine.

100% genuine

contact us today! deals this good don't last forever.

email: clothoffer@mailverno.com

Please use the images that I have attached on the flyer accordingly. Also feel free to be as creative as possible I want it to attract a lot of attention but also look professional so you may add some things to improve the look of the flyer.

note: the product being sold is on the pictures I've provided, in particular, i want file 2 "main image" in a large size on the flyer!

thank you! and happy holidays

Target Market(s)

Muslims and Islamic collectors

Industry/Entity Type

House

Requirements
Must have
• the dimensions of the flyer is :
• A5 horizontal or vertical
• (210 x 148 mm)
• must have colors! up to you what colors to choose!

```html
<!DOCTYPE html>
<html lang="en">
<head>
<meta charset="utf-8">
<title>Rare Kiswah For Sale – Flyer</title>
<link href="https://fonts.googleapis.com/css2?family=Archivo+Black&family=Arimo:wght@700&display=swap" rel="stylesheet">
<style>
  :root {
    --gold: #c4952f;
    --gold-light: #e6b52a;
    --gold-deep: #a87d24;
    --ink: #151515;
    --ink-soft: #222;
    --white: #ffffff;
    --stage: #efece6;
  }
  html, body {
    margin: 0;
    padding: 0;
    width: 960px;
    height: 1200px;
    overflow: hidden;
    background: var(--stage);
  }
  .stage {
    position: relative;
    width: 960px;
    height: 1200px;
  }
  .flyer {
    position: absolute;
    left: 68px;
    top: 12px;
    width: 975px;
    height: 1380px;
    transform: scale(0.8522);
    transform-origin: top left;
    overflow: hidden;
    background: var(--gold);
    font-family: "Arimo", Arial, sans-serif;
    font-weight: 700;
    color: var(--white);
  }
  .flyer-art {
    position: absolute;
    inset: 0;
  }
  .badge {
    position: absolute;
    left: 13px;
    top: 18px;
    width: 400px;
    text-align: center;
    font-family: "Archivo Black", Arial, sans-serif;
    color: var(--gold);
    line-height: 1;
  }
  .badge-top { font-size: 68px; display: block; }
  .badge-bottom { font-size: 54px; display: block; margin-top: 12px; }
  .title {
    position: absolute;
    left: 455px;
    top: 88px;
    font-family: "Archivo Black", Arial, sans-serif;
    color: var(--gold);
    -webkit-text-stroke: 2px #3a2a08;
    line-height: 1;
  }
  .title-main { font-size: 70px; display: block; }
  .title-of { font-size: 38px; display: block; margin-top: 4px; }
  .title-kaaba { font-size: 80px; display: inline-block; margin-top: -2px; }
  .title-sale { font-size: 36px; }
  .title-vintage {
    display: block;
    font-family: "Arimo", Arial, sans-serif;
    -webkit-text-stroke: 0;
    color: var(--white);
    font-size: 26px;
    margin-top: 6px;
  }
  .kaaba-note {
    position: absolute;
    left: 250px;
    width: 700px;
    top: 610px;
    text-align: center;
    font-size: 31px;
    line-height: 39px;
  }
  .product-note {
    position: absolute;
    left: 412px;
    width: 530px;
    top: 782px;
    text-align: center;
    font-size: 23.5px;
    line-height: 30.5px;
  }
  .price-list {
    position: absolute;
    left: 325px;
    top: 975px;
    margin: 0;
    padding: 0;
    list-style: none;
    font-size: 25px;
    line-height: 32px;
  }
  .assurance {
    position: absolute;
    left: 150px;
    width: 810px;
    top: 1120px;
    text-align: center;
    font-size: 26px;
    line-height: 33px;
  }
  .contact {
    position: absolute;
    left: 120px;
    width: 870px;
    top: 1264px;
    text-align: center;
  }
  .contact-call { font-size: 30px; display: block; line-height: 40px; }
  .contact-email { font-size: 35px; display: block; line-height: 44px; }
</style>
</head>
<body>
<div class="stage">
  <div class="flyer">
    <svg class="flyer-art" viewBox="0 0 975 1380" width="975" height="1380" aria-hidden="false">
      <defs>
        <linearGradient id="kaabaTone" x1="0" y1="0" x2="1" y2="1">
          <stop offset="0" stop-color="#0f0f0f"/>
          <stop offset="0.55" stop-color="#1e1a12"/>
          <stop offset="1" stop-color="#2b2316"/>
        </linearGradient>
        <linearGradient id="clothTone" x1="0" y1="0" x2="1" y2="1">
          <stop offset="0" stop-color="#5d6062"/>
          <stop offset="0.5" stop-color="#9a9d9f"/>
          <stop offset="1" stop-color="#6c6f71"/>
        </linearGradient>
        <linearGradient id="contactBand" x1="0" y1="0" x2="1" y2="0">
          <stop offset="0" stop-color="#c89a2c"/>
          <stop offset="0.5" stop-color="#e9b51f"/>
          <stop offset="1" stop-color="#c89a2c"/>
        </linearGradient>
      </defs>

      <!-- base gold -->
      <rect class="base" width="975" height="1380" fill="var(--gold)"/>

      <!-- Kaaba photograph area -->
      <rect class="kaaba-photo" role="img" aria-label="Photograph of the Kaaba draped in its black Kiswah with gold embroidered calligraphy and door curtain" x="400" y="0" width="575" height="770" fill="url(#kaabaTone)"/>

      <!-- gold corner on right -->
      <polygon points="975,520 975,770 760,770" fill="var(--gold)"/>

      <!-- black lower band behind product text -->
      <rect x="0" y="765" width="975" height="193" fill="var(--ink)"/>

      <!-- translucent caption band -->
      <polygon points="250,598 975,598 975,758 250,758" fill="rgba(85,62,12,0.78)"/>

      <!-- lower gold area -->
      <rect x="0" y="958" width="975" height="422" fill="var(--gold)"/>

      <!-- diagonal stripes -->
      <polygon points="0,190 30,190 480,765 410,765 0,255" fill="var(--gold)"/>
      <polygon points="30,300 110,230 570,765 500,765" fill="var(--ink)"/>
      <polygon points="110,230 140,205 600,765 570,765" fill="var(--gold)"/>
      <polygon points="140,205 185,170 650,765 600,765" fill="var(--ink)"/>
      <polygon points="185,170 215,145 690,765 650,765" fill="var(--gold)"/>
      <polygon points="0,300 30,300 500,765 440,765 0,350" fill="var(--gold)"/>

      <!-- top stripes over photo -->
      <polygon points="335,0 470,0 430,45 300,45" fill="var(--gold)"/>
      <polygon points="330,0 360,0 230,150 200,150" fill="var(--ink)"/>
      <polygon points="380,0 470,0 400,90 330,90" fill="var(--gold)"/>
      <polygon points="420,0 470,0 370,120 340,120" fill="var(--ink)"/>

      <!-- product cloth photograph -->
      <polygon class="cloth-photo" role="img" aria-label="Photograph of grey Kiswah silk woven with Quranic calligraphy" points="0,355 390,840 0,1330" fill="url(#clothTone)"/>

      <!-- gold edge below cloth -->
      <polygon points="390,840 0,1330 0,1380 45,1380 300,1055 420,1000" fill="var(--gold)"/>
      <polygon points="0,1330 0,1380 60,1380 200,1200" fill="var(--gold-deep)" opacity="0.4"/>

      <!-- contact band -->
      <rect x="120" y="1262" width="855" height="90" fill="url(#contactBand)"/>

      <!-- badge diamond -->
      <polygon points="8,88 213,-126 418,88 213,302" fill="var(--ink)" stroke="var(--white)" stroke-width="4"/>
    </svg>

    <div class="badge">
      <span class="badge-top">100%</span>
      <span class="badge-bottom">GENUINE</span>
    </div>

    <h1 class="title" style="margin:0;font-weight:400;">
      <span class="title-main">Rare Kiswah</span>
      <span class="title-of">Of The Holy</span>
      <span class="title-kaaba">KAABA</span><span class="title-sale">For Sale</span>
      <span class="title-vintage">(Fitted In 1977 And 1982 Vintage)</span>
    </h1>

    <p class="kaaba-note" style="margin:0;">The Kaaba is covered by an expensive black cloth which is known as 'Kiswah' which is produced and changed every year</p>

    <p class="product-note" style="margin:0;">Silk lampas weave Kiswah, woven silk on a black satin ground with Quranic calligraphy, the zig-zag bands of inscription alternate with the Shahadah and the inscription, 'God, exalted be His Glory!</p>

    <ol class="price-list">
      <li>1) whole piece 15 meters x 2.60 meters : £60,000</li>
      <li>2) 8 meters x 2.60 meters : £31,200</li>
      <li>3) 4 meters x 2.60 meters : £15,600</li>
      <li>4) 1 meter : £1500</li>
    </ol>

    <p class="assurance" style="margin:0;">Harwell's international auction house authenticity document also available to prove the Kiswah is genuine. please note a percentage of sales will go towards Sadaqah for our Muslim brothers and sisters in need around the world</p>

    <p class="contact" style="margin:0;">
      <span class="contact-call">contact us today! deals this good don't last forever.</span>
      <span class="contact-email">Email: clothoffer@mailverno.com</span>
    </p>
  </div>
</div>
</body>
</html>
```